RW Skyline Imaging Web Site design

I am looking for a responsive single page website deign for rwskylineimages.example. This is a drone based aerial photography and cinematography business. It should have an about us section, a services section that contains photograph service, Video footage, and Aerial mapping all under the services section, a pricing section, and then a contact page for customers to contact us.

Coding

Coded - Design and coding required

Number of Pages Required

1 page

Font styles to use
Sans Serif

Colors

Designer to choose colors to be used in the design.

Requirements
Must have
• Responsive design. About us section, services section, pricing section under the services links, and contact us section, that links to a submission page where they can send Name, address, email, and comments on what they are interested in.
• See flyquad7x.example - looking for similar design.
Should not have
• clutter, or too busy design

```html
<!DOCTYPE html>
<html lang="en">
<head>
<meta charset="utf-8">
<title>RW Skyline Imaging</title>
<link rel="stylesheet" href="https://fonts.googleapis.com/css2?family=Montserrat:wght@400;500;600;700&family=Playfair+Display:ital,wght@0,400;1,400;1,700&display=swap">
<style>
  :root {
    --ink: #111111;
    --muted: #666666;
    --white: #ffffff;
    --accent: #f0901e;
    --hero-top: #24242b;
    --hero-bottom: #3a4038;
    --city-top: #1d2326;
    --city-bottom: #2f3a3c;
    --footer: #c9c9c9;
    --footer-ink: #8a8a8a;
    --line: #dddddd;
  }
  * { box-sizing: border-box; margin: 0; padding: 0; }
  html, body { width: 1200px; height: 2209px; overflow: hidden; }
  body { position: relative; background: var(--white); font-family: "Montserrat", sans-serif; color: var(--ink); }

  .hero { position: absolute; left: 0; top: 0; width: 1200px; height: 467px; }
  .hero-backdrop { position: absolute; inset: 0; background: radial-gradient(ellipse at 30% 25%, #6a6870 0%, transparent 45%), linear-gradient(180deg, var(--hero-top), #2c302c 60%, var(--hero-bottom)); }
  .social-top { position: absolute; left: 26px; top: 36px; display: flex; gap: 12px; }
  .social-top span { width: 9px; height: 9px; border-radius: 50%; background: #cfcfcf; }
  .nav { position: absolute; top: 35px; font-size: 10px; color: var(--white); letter-spacing: .3px; }
  .nav.active { border-bottom: 1px solid var(--white); padding-bottom: 3px; }
  .brand { position: absolute; left: 0; width: 1200px; top: 28px; text-align: center; color: var(--white); }
  .brand-dot { display: inline-block; width: 12px; height: 12px; border-radius: 50%; background: var(--accent); vertical-align: middle; margin-right: 6px; }
  .brand-name { font-size: 10px; letter-spacing: 3px; vertical-align: middle; }
  .hero-title { position: absolute; left: 0; width: 1200px; top: 230px; text-align: center; font-family: "Playfair Display", serif; font-weight: 400; font-size: 74px; line-height: 1.1; color: var(--white); }
  .hero-tagline { position: absolute; left: 0; width: 1200px; top: 325px; text-align: center; font-size: 13px; font-weight: 700; color: var(--white); }
  .hero-tagline em { font-family: "Playfair Display", serif; }

  .about { position: absolute; left: 0; top: 467px; width: 1200px; height: 471px; }
  .about-media { position: absolute; left: 175px; top: 112px; width: 374px; height: 238px; background: linear-gradient(180deg, #d8d2d8 0%, #b9b6bd 35%, #6f7c80 50%, #4d6a3d 70%, #3d5a2e 100%); box-shadow: 0 20px 40px rgba(0,0,0,.18); }
  .play { position: absolute; left: 163px; top: 95px; }
  .about h2 { position: absolute; left: 610px; top: 110px; font-size: 40px; font-weight: 700; }
  .about-lead { position: absolute; left: 610px; top: 163px; width: 420px; font-size: 10px; line-height: 1.35; color: #333; }
  .feature { position: absolute; width: 190px; }
  .feature h3 { font-family: "Playfair Display", serif; font-weight: 400; font-size: 12px; margin-bottom: 10px; }
  .feature p { font-size: 10px; line-height: 1.3; color: var(--muted); }

  .pricing { position: absolute; left: 0; top: 938px; width: 1200px; height: 777px; }
  .pricing-backdrop { position: absolute; inset: 0; background: linear-gradient(180deg, var(--city-top), #263033 45%, var(--city-bottom)); }
  .plan { position: absolute; top: 213px; width: 271px; height: 349px; border: 1.5px solid rgba(255,255,255,.85); color: var(--white); text-align: center; }
  .plan-name { margin-top: 44px; font-family: "Playfair Display", serif; font-size: 12px; }
  .plan-price { font-size: 50px; font-weight: 400; line-height: 1.1; margin-top: 2px; }
  .plan-unit { font-size: 15px; margin-top: 2px; }
  .plan-desc { font-size: 10px; line-height: 1.3; width: 190px; margin: 40px auto 0; }
  .plan-button { display: inline-block; margin-top: 30px; width: 113px; height: 32px; line-height: 30px; border: 1.5px solid var(--white); border-radius: 16px; font-size: 9px; font-weight: 700; letter-spacing: .5px; }

  .contact { position: absolute; left: 0; top: 1715px; width: 1200px; height: 449px; }
  .field { position: absolute; left: 218px; width: 327px; border-bottom: 1px solid var(--line); font-size: 10px; color: #999; padding-bottom: 14px; }
  .send { position: absolute; left: 218px; top: 376px; width: 62px; height: 30px; line-height: 30px; border-radius: 15px; background: var(--accent); color: var(--white); text-align: center; font-size: 9px; font-weight: 700; }
  .contact h2 { position: absolute; left: 670px; top: 52px; font-size: 30px; font-weight: 700; }
  .contact-lead { position: absolute; left: 670px; top: 100px; width: 300px; font-size: 10px; line-height: 1.35; color: var(--muted); }
  .office { position: absolute; left: 670px; top: 146px; font-size: 10px; line-height: 1.5; color: var(--muted); }
  .office h3 { font-family: "Playfair Display", serif; font-weight: 400; font-size: 12px; color: var(--ink); margin-bottom: 6px; }

  .footer { position: absolute; left: 0; top: 2164px; width: 1200px; height: 45px; background: var(--footer); }
  .copyright { position: absolute; left: 177px; top: 17px; font-size: 8px; color: var(--footer-ink); }
  .social-bottom { position: absolute; left: 832px; top: 18px; display: flex; gap: 14px; }
  .social-bottom span { width: 10px; height: 10px; border-radius: 50%; background: var(--footer-ink); }
</style>
</head>
<body>

<header class="hero">
  <div class="hero-backdrop" role="img" aria-label="Misty evergreen forest seen from above"></div>
  <div class="social-top"><span></span><span></span><span></span></div>
  <span class="nav active" style="left:418px">HOME</span>
  <span class="nav" style="left:464px">ABOUT</span>
  <div class="brand"><span class="brand-dot"></span><span class="brand-name">RW Skyline Imaging</span></div>
  <span class="nav" style="left:700px">PRICING</span>
  <span class="nav" style="left:758px">CONTACT</span>
  <h1 class="hero-title">RW Skyline Imaging</h1>
  <p class="hero-tagline"><em>Welcome</em> Folks.</p>
</header>

<section class="about">
  <div class="about-media" role="img" aria-label="Coastal headland with flowering shrubs above the sea">
    <svg class="play" width="48" height="48" viewBox="0 0 48 48">
      <circle cx="24" cy="24" r="24" fill="#f0901e"/>
      <path d="M20 17 L31 24 L20 31 Z" fill="#ffffff"/>
    </svg>
  </div>
  <h2>About us</h2>
  <p class="about-lead">We are RW Skyline - The best drone photography company with great drone pilots. We capture land, sea and city from above with care. Every flight is planned, safe and fully insured.</p>
  <div class="feature" style="left:610px;top:240px"><h3>Design</h3><p>Every flight is planned around your site, your light and your story.</p></div>
  <div class="feature" style="left:820px;top:240px"><h3>Develop</h3><p>Every flight is planned around your site, your light and your story.</p></div>
  <div class="feature" style="left:610px;top:344px"><h3>Deploy</h3><p>Every flight is planned around your site, your light and your story.</p></div>
  <div class="feature" style="left:820px;top:344px"><h3>Support</h3><p>Every flight is planned around your site, your light and your story.</p></div>
</section>

<section class="pricing">
  <div class="pricing-backdrop" role="img" aria-label="Night city skyline of towers seen from a drone"></div>
  <div class="plan" style="left:175px">
    <p class="plan-name">Drone Photography</p>
    <p class="plan-price">$200</p>
    <p class="plan-unit">IMAGES</p>
    <p class="plan-desc">Up to 20 edited high resolution images. Available Drone Photography services include editing, titling, and more.</p>
    <span class="plan-button">CONTACT</span>
  </div>
  <div class="plan" style="left:464px">
    <p class="plan-name">Drone Videography</p>
    <p class="plan-price">$200</p>
    <p class="plan-unit">RAW FOOTAGE</p>
    <p class="plan-desc">Raw aerial footage available for you to use. Available Drone Videography services include filming, editing, music, titling and more.</p>
    <span class="plan-button">CONTACT</span>
  </div>
  <div class="plan" style="left:752px">
    <p class="plan-name">3D Mapping</p>
    <p class="plan-price">$200</p>
    <p class="plan-unit">3D MODEL</p>
    <p class="plan-desc">Amazing Aerial 3D Models for you to use. Available 3D Mapping services include 2D Maps, and 3D Models.</p>
    <span class="plan-button">CONTACT</span>
  </div>
</section>

<section class="contact">
  <div class="field" style="top:148px">Your Email (required)</div>
  <div class="field" style="top:224px">Subject</div>
  <div class="field" style="top:303px">Your Message</div>
  <div class="send">SEND</div>
  <h2>Contact</h2>
  <p class="contact-lead">Tell us about your project and we will reply within one business day with a plan and a quote.</p>
  <div class="office">
    <h3>Northfield Bay</h3>
    <p>Mon – Fri, 9am – 6pm</p>
    <p>Call ahead for site visits</p>
    <p style="margin-top:22px">48 Harbor Ln. Suite 3B</p>
    <p>hello@rwskyline.example</p>
  </div>
</section>

<footer class="footer">
  <p class="copyright">© 2017 RW Skyline Imaging. All Rights Reserved.</p>
  <div class="social-bottom"><span></span><span></span><span></span><span></span><span></span><span></span><span></span><span></span></div>
</footer>

</body>
</html>
```